Larkmoor Personal Styling Agency needs ad for Fairway Quarterly

We are a boutique personal styling and personal shopping agency based out of San Francisco, called Corvale Personal Image Consulting. We specialize in outfitting senior leaders in tech, helping them create images that endure and a personal styling with impact. People work with us so the world sees them as they want to be perceived. Our packages are listed on our site http://corvale-consulting.example/ under services.

There are great reviews here: https://www.reviewnest.example/biz/corvale-personal-image-consulting-oakvale-2

Our clientele is 60% female and 40% male. We need this ad to speak to both sexes. Our goal is to have people reach out to us and schedule consultations. The design should have a luxury feel and should have a design that is consistent with our website.

This ad is for a Fairway Quarterly. If people reach out to us and mention the Teeplume they get $100 off their first package. The attached add is what the Fairway Quarterly company came up with. It is a chintzy and too obvious - not what we want, but might be useful for dimension, phone number and email.

Target Market(s)

Men and women ages 36-65 in the greater San Francisco Bay area who are members of golf clubs and make upward of $150k/yr.

Industry/Entity Type

Shopping

Font styles to use
Sans Serif

Requirements
Must have
• Say - Mention "Teeplume" to get $100 off your first package
• Have phone number, website and email address
• Corvale logo
• Be consistent with the look and feel of the website

```html
<!DOCTYPE html>
<html lang="en">
<head>
<meta charset="utf-8">
<title>Corvale Personal Image Consulting – Fairway Quarterly Ad</title>
<link rel="stylesheet" href="https://fonts.googleapis.com/css2?family=Nunito+Sans:wght@300;400;600&display=swap">
<style>
  :root {
    --mist: #dcdfe4;
    --paper: #ffffff;
    --ink: #2b2b2b;
    --gold: #d4a514;
    --gold-text: #d9a92a;
    --wood-light: #f3c98a;
    --wood-deep: #e9a24e;
    --white: #ffffff;
  }
  * { margin: 0; padding: 0; box-sizing: border-box; }
  html, body { width: 786px; height: 1200px; overflow: hidden; background: var(--paper); }
  body { font-family: "Nunito Sans", sans-serif; }

  .ad { position: relative; width: 786px; height: 1200px; overflow: hidden; }

  .hero { position: absolute; left: 0; top: 0; width: 786px; height: 1032px; background: var(--mist); }

  .hanger-photo { position: absolute; left: 146px; top: 126px; width: 492px; height: 270px; }

  .headline {
    position: absolute; left: 0; top: 444px; width: 786px;
    text-align: center; color: var(--white);
    font-weight: 400; font-size: 52px; line-height: 76px; letter-spacing: 0.5px;
    text-shadow: 0 1px 6px rgba(0,0,0,0.08);
  }
  .headline .accent { position: relative; font-weight: 600; }
  .headline .accent::after {
    content: ""; position: absolute; left: 0; right: 0; bottom: -4px;
    height: 4px; background: var(--gold);
  }

  .offer {
    position: absolute; left: 0; top: 906px; width: 786px;
    text-align: center; color: var(--white);
    font-weight: 400; font-size: 26px; line-height: 42px; letter-spacing: 1px;
  }
  .offer .accent { position: relative; font-weight: 600; }
  .offer .accent::after {
    content: ""; position: absolute; left: 0; right: 0; bottom: -1px;
    height: 3px; background: var(--gold);
  }

  .footer { position: absolute; left: 0; top: 1032px; width: 786px; height: 168px; background: var(--paper); }

  .brand { position: absolute; left: 34px; top: 44px; display: flex; align-items: center; }
  .brand-dot { width: 46px; height: 46px; border-radius: 50%; background: var(--gold); margin-right: 24px; }
  .brand-name {
    font-weight: 300; font-size: 34px; letter-spacing: 8px; color: var(--ink); line-height: 38px;
  }
  .brand-tagline {
    font-weight: 300; font-size: 11px; letter-spacing: 2px; color: var(--ink); margin-top: 8px;
  }

  .contact {
    position: absolute; right: 36px; top: 34px; text-align: right;
    color: var(--gold-text); font-weight: 300;
  }
  .contact .mission { font-size: 14px; line-height: 21px; letter-spacing: 0.3px; }
  .contact .site { font-size: 14px; margin-top: 21px; letter-spacing: 0.3px; }
  .contact .reach { font-size: 12.5px; margin-top: 6px; letter-spacing: 0.3px; }
</style>
</head>
<body>
<main class="ad">
  <section class="hero">
    <svg class="hanger-photo" viewBox="0 0 492 270" role="img" aria-label="Photograph of an empty wooden clothes hanger with a metal hook">
      <defs>
        <radialGradient id="woodGlow" cx="50%" cy="60%" r="55%">
          <stop offset="0%" stop-color="var(--wood-deep)" stop-opacity="0.55"/>
          <stop offset="60%" stop-color="var(--wood-light)" stop-opacity="0.35"/>
          <stop offset="100%" stop-color="var(--wood-light)" stop-opacity="0"/>
        </radialGradient>
      </defs>
      <rect x="0" y="0" width="492" height="270" fill="url(#woodGlow)"/>
    </svg>

    <h1 class="headline"><span class="accent">Love</span> your wardrobe<br>today.</h1>

    <p class="offer">Get <span class="accent">$100 OFF</span> your first package<br>when you mention “Teeplume”.</p>
  </section>

  <footer class="footer">
    <div class="brand">
      <div class="brand-dot"></div>
      <div>
        <div class="brand-name">CORVALE</div>
        <div class="brand-tagline">PERSONAL IMAGE CONSULTING</div>
      </div>
    </div>

    <div class="contact">
      <p class="mission">Celebrating 12 years of helping men and women<br>curate personal styles that impact.</p>
      <p class="site">www.corvale-consulting.example</p>
      <p class="reach">415-555-0142 / studio@corvale-consulting.example</p>
    </div>
  </footer>
</main>
</body>
</html>
```